Insurance company needs a business card design

We need a business card design for a Massachusetts-based insurance company Cielora Insurance, LLC. We provide auto insurance to Hispanic (Spanish- or Portuguese-speaking) immigrants in the United States. We will give these business cards to auto dealers where such customers typically go to purchase vehicles. We will provide a solution to the dealers to provide easy insurance to the customers buying cars at their dealerships. Cielora is the Spanish word for protection.
Contact Information for Business Card
Name, Designation, Company Name, Address, Phone Number, Email, Website
Look and feel
Each slider illustrates characteristics of the customer's brand and the style your logo design should communicate.

```html
<!DOCTYPE html>
<html lang="en">
<head>
<meta charset="utf-8">
<title>Cielora Insurance – Business Card</title>
<link rel="stylesheet" href="https://fonts.googleapis.com/css2?family=Montserrat:wght@600;700;800&family=Arimo:wght@400&display=swap">
<style>
  :root {
    --navy: #0b4a80;
    --navy-deep: #083d6b;
    --orange: #f08a24;
    --white: #ffffff;
    --ink: #1f2a36;
    --stage: #2e2926;
  }
  * { box-sizing: border-box; margin: 0; padding: 0; }
  html, body { width: 1200px; height: 822px; overflow: hidden; }
  body {
    background: var(--stage);
    display: flex;
    align-items: center;
    justify-content: center;
    gap: 40px;
    font-family: "Arimo", Arial, sans-serif;
  }
  .card {
    position: relative;
    width: 540px;
    height: 309px;
    border-radius: 22px;
    overflow: hidden;
  }

  /* Back side */
  .card-back { background: var(--navy); }
  .back-pattern {
    position: absolute; inset: 0;
    background: linear-gradient(135deg, var(--navy) 0%, var(--navy-deep) 100%);
  }
  .back-wordmark {
    position: absolute;
    right: 34px; bottom: 92px;
    font-family: "Montserrat", sans-serif;
    font-weight: 800;
    font-size: 26px;
    letter-spacing: 0.5px;
    color: var(--white);
    text-transform: uppercase;
  }

  /* Front side */
  .card-front { background: var(--white); color: var(--ink); }
  .front-wordmark {
    position: absolute;
    left: 38px; top: 52px;
    font-family: "Montserrat", sans-serif;
    font-weight: 800;
    font-size: 34px;
    line-height: 1;
    color: var(--navy);
    text-transform: uppercase;
  }
  .band {
    position: absolute;
    left: 0; right: 0; top: 128px; height: 74px;
    display: flex;
  }
  .band-main {
    flex: 0 0 410px;
    background: var(--navy);
    padding: 14px 0 0 40px;
    color: var(--white);
  }
  .band-accent { flex: 1; background: var(--orange); }
  .person-name {
    font-family: "Montserrat", sans-serif;
    font-weight: 800;
    font-size: 22px;
    letter-spacing: 0.5px;
    text-transform: uppercase;
  }
  .person-title { font-size: 14px; margin-top: 4px; }
  .contacts {
    position: absolute;
    left: 40px; bottom: 30px;
    list-style: none;
    font-size: 14px;
  }
  .contacts li {
    display: flex; align-items: center; gap: 10px;
    margin-top: 8px;
  }
  .contacts svg { width: 14px; height: 14px; flex: none; }
  .web-name { color: var(--orange); }
  .address {
    position: absolute;
    right: 36px; top: 222px;
    font-size: 14px;
    line-height: 1.45;
    text-align: right;
    font-style: normal;
  }
</style>
</head>
<body>

<section class="card card-back" aria-label="Card back">
  <div class="back-pattern" role="img" aria-label="Repeating faint brand-shield pattern on navy"></div>
  <div class="back-wordmark">Cielora Insurance</div>
</section>

<section class="card card-front" aria-label="Card front">
  <div class="front-wordmark">Cielora Insurance</div>

  <div class="band">
    <div class="band-main">
      <div class="person-name">Tomas Rivera</div>
      <div class="person-title">Managing Director</div>
    </div>
    <div class="band-accent"></div>
  </div>

  <address class="address">
    4218 Linden Avenue<br>
    Country Name, AB 29531
  </address>

  <ul class="contacts">
    <li>
      <svg viewBox="0 0 16 16" aria-hidden="true"><path fill="#0b4a80" d="M3.6 1.5l2.3 2.6-1.3 1.8c.9 1.9 2.5 3.5 4.4 4.4l1.8-1.3 2.6 2.3-1.4 2.4C7 13.3 2.7 9 2.3 4.1z"/></svg>
      (123) 555-0187
    </li>
    <li>
      <svg viewBox="0 0 16 16" aria-hidden="true"><rect x="1" y="3" width="14" height="10" rx="1" fill="#0b4a80"/><path d="M1.5 3.8L8 9l6.5-5.2" stroke="#fff" stroke-width="1.3" fill="none"/></svg>
      info@cielorainsurance.com
    </li>
    <li>
      <svg viewBox="0 0 16 16" aria-hidden="true"><circle cx="8" cy="8" r="6.5" fill="#0b4a80"/><path d="M1.5 8h13M8 1.5c-3 3.5-3 9.5 0 13M8 1.5c3 3.5 3 9.5 0 13" stroke="#fff" stroke-width="1" fill="none"/></svg>
      <span>www.<span class="web-name">cielorainsurance</span>.com</span>
    </li>
  </ul>
</section>

</body>
</html>
```